Real Estate Agent - Sold Brochure

I am a Real Estate Agent who is looking for a SOLD brochure design that looks simple, sharp, classy and elegant. Over the years, I have created a business image for myself that has helped me sell a lot of top end properties with great results. "Cheerful Mara, Cheerful Buyer" is my logo and the message that I consistently portray to my clients in my area.
I am after a double-sided brochure. On the front I would like a photo of the SOLD property with a watermark "not just sold....sold for a premium". It will also have my company logo, with personal profile photo and personal logo - "Cheerful Mara, Cheerful Buyer".
On the back, I would like the client testimonial letter and the client sold photo - as well as my personal logo once again - "Cheerful Mara, Cheerful Buyer".
If you could exercise your artistic imagination as a designer and create something classy and extraordinary.
Please see attached samples of work created previously and feel free to come up with new ideas or improvements.

Additional details: Flyer size to be approx. landscape layout 240mm wide x 130mm high.

Many thanks,
Mara

Additional details: Flyer size to be approx. landscape layout 240mm wide x 130mm high. with rounded corners

```html
<!DOCTYPE html>
<html lang="en">
<head>
<meta charset="utf-8">
<title>Sold Brochure – Cheerful Mara, Cheerful Buyer</title>
<link rel="stylesheet" href="https://fonts.googleapis.com/css2?family=Arimo:wght@700&family=EB+Garamond:ital,wght@0,400;0,500;1,400&family=Questrial&display=swap">
<style>
  :root {
    --backdrop: #404040;
    --plum: #a85a86;
    --cream: #f6ebe1;
    --paper: #fbf6ef;
    --rule: #ecd9c6;
    --ink: #3b3330;
    --logo-ink: #3a3a3a;
    --gold: #e8a524;
    --white: #ffffff;
  }
  * { box-sizing: border-box; margin: 0; padding: 0; }
  html, body { width: 1077px; height: 1200px; overflow: hidden; }
  body { background: var(--backdrop); position: relative; font-family: "EB Garamond", Georgia, serif; }

  .side { position: absolute; left: 48px; width: 981px; height: 532px; border-radius: 10px; overflow: hidden; }
  .side--front { top: 50px; background: var(--cream); }
  .side--back { top: 619px; background: var(--plum); }

  /* front */
  .property-photo { position: absolute; left: 0; top: 0; width: 607px; height: 404px;
    background: linear-gradient(180deg, #4f86c9 0%, #9fc3ea 30%, #a0634e 45%, #7b5646 62%, #3f7a35 78%, #5b8c3c 100%); }
  .headline { position: absolute; left: 650px; top: 92px; color: var(--plum); font-family: "Questrial", Arial, sans-serif;
    font-weight: 400; line-height: 0.95; text-shadow: 2px 2px 2px rgba(90,40,60,.35); }
  .headline span { display: block; }
  .headline .l1 { font-size: 34px; }
  .headline .l2 { font-size: 66px; margin-bottom: 14px; }
  .headline .l3 { font-size: 34px; padding-left: 58px; }
  .headline .l4 { font-size: 52px; padding-left: 58px; }
  .front-band { position: absolute; left: 0; top: 404px; width: 981px; height: 128px; background: var(--plum); }
  .tagline { color: var(--white); font-style: italic; font-weight: 400; white-space: nowrap; }
  .front-band .tagline { position: absolute; left: 34px; top: 40px; font-size: 33px; }
  .agent-portrait { position: absolute; left: 475px; top: 153px; width: 235px; height: 379px;
    border-radius: 110px 110px 0 0; background: linear-gradient(180deg, #3a2620 0%, #d9b49c 35%, #f4f1ee 55%, #ececec 100%); }

  .brand { position: absolute; background: var(--white); display: flex; flex-direction: column; justify-content: center; padding-left: 14px; }
  .brand__row { display: flex; align-items: center; gap: 10px; }
  .brand__name { font-weight: 500; color: var(--logo-ink); font-size: 21px; letter-spacing: .3px; white-space: nowrap; }
  .brand__mark { width: 52px; height: 52px; border-radius: 50%; background: var(--gold); flex: none; }
  .brand__sub { font-size: 10.5px; letter-spacing: 1.4px; color: var(--logo-ink); border-top: 1px solid #999; width: 160px; margin-top: -10px; padding-top: 2px; white-space: nowrap; }
  .brand__web { font-size: 12px; font-weight: 500; color: var(--logo-ink); margin-top: 10px; letter-spacing: .5px; }
  .side--front .brand { left: 710px; top: 404px; width: 271px; height: 128px; }
  .side--back .brand { left: 620px; top: 333px; width: 255px; height: 111px; padding-left: 12px; }
  .side--back .brand__name { font-size: 20px; }
  .side--back .brand__mark { width: 48px; height: 48px; }

  /* back */
  .testimonial { position: absolute; left: 28px; top: 12px; width: 522px; height: 512px; transform: rotate(-1.6deg);
    background: var(--paper); box-shadow: 4px 6px 10px rgba(0,0,0,.3); padding: 100px 70px 0 84px; color: var(--ink); font-size: 13.5px; line-height: 23px;
    background-image: repeating-linear-gradient(180deg, transparent 0 22px, var(--rule) 22px 23px); background-position: 0 100px; }
  .testimonial p { text-align: justify; margin-bottom: 23px; }
  .testimonial .address { margin-bottom: 18px; }
  .testimonial .signature { margin: 0; }
  .paperclip { position: absolute; left: 46px; top: -8px; width: 22px; height: 60px; }
  .sold-photo { position: absolute; left: 562px; top: 0; width: 371px; height: 278px;
    background: linear-gradient(180deg, #3c6fb9 0%, #9dbde0 35%, #8e6a4c 50%, #6d5a4a 70%, #6d8a48 100%); }
  .side--back .tagline { position: absolute; left: 622px; top: 292px; font-size: 25px; }
  .contact { position: absolute; left: 624px; top: 455px; display: flex; align-items: center; color: var(--white); font-family: "Arimo", Arial, sans-serif; font-weight: 700; }
  .contact__agent { font-size: 17px; line-height: 19px; padding-right: 10px; border-right: 2px solid var(--white); }
  .contact__office { font-size: 25px; padding-left: 10px; }
</style>
</head>
<body>
  <section class="side side--front">
    <div class="property-photo" role="img" aria-label="Photo of the sold brick house with green roof and hedged garden"></div>
    <h1 class="headline">
      <span class="l1">NOT JUST</span>
      <span class="l2">SOLD....</span>
      <span class="l3">SOLD FOR A</span>
      <span class="l4">PREMIUM</span>
    </h1>
    <div class="front-band"><p class="tagline">Cheerful Mara, Cheerful Buyer</p></div>
    <div class="agent-portrait" role="img" aria-label="Portrait of agent Mara in a white jacket"></div>
    <div class="brand">
      <div class="brand__row"><span class="brand__name">HARBOUR &amp; VALE</span><span class="brand__mark"></span></div>
      <span class="brand__sub">REAL ESTATE AGENTS</span>
      <span class="brand__web">www.harbourvale.com.au</span>
    </div>
  </section>

  <section class="side side--back">
    <article class="testimonial">
      <svg class="paperclip" viewBox="0 0 22 60" aria-hidden="true"><path d="M6 40 V10 a5 5 0 0 1 10 0 V48 a7 7 0 0 1 -14 0 V16" fill="none" stroke="#e89a2c" stroke-width="2.5" stroke-linecap="round"/></svg>
      <p class="address">24 Banksia Crescent, Redwood</p>
      <p>After having the house on sale with various other agents and receiving only lukewarm service and low offers we were very impressed with your sale strategy which resulted in the best open house we ever had and multiple good offers, some higher than the asking price leading to us accepting a good offer and being able to move on.</p>
      <p>We have already recommended your services to a neighbour who is thinking of selling and would be comfortable in recommending your services to anyone in the area thinking of selling. It was a real pleasure to have had you represent our interested in the sale of our house.</p>
      <p class="signature">Delia Marsh</p>
    </article>
    <div class="sold-photo" role="img" aria-label="Photo of the sellers with Mara beside the sold sign in front of the house"></div>
    <p class="tagline">Cheerful Mara, Cheerful Buyer</p>
    <div class="brand">
      <div class="brand__row"><span class="brand__name">HARBOUR &amp; VALE</span><span class="brand__mark"></span></div>
      <span class="brand__sub">REAL ESTATE AGENTS</span>
      <span class="brand__web">www.harbourvale.com.au</span>
    </div>
    <div class="contact">
      <div class="contact__agent">Mara Tanner<br>0400 555 218</div>
      <div class="contact__office">3700 5501</div>
    </div>
  </section>
</body>
</html>
```